Kelvora - consultancy website

I need a new design for my webpage/presence [to be functioning with Wordpress - I have a programmer to set it up but not the design idea].
My company is Kelvora - a consultancy firm focused on growth management for Swedish SME's primarily;. We call it Leadership add-on for firms on the rise, kind of a doctor helping small become big. Contentwise, its a simple frontpage + 3-4 subpages with content re company/myself/focus etc. The new site should communicate a fresh, trustworthy take yet simple and functional on all devices [i.e. think UI compatible for mobile/tablet]. Current building parts/form elements are
a) existing logo and text elements
b) existing pictures
c) the yellowish color
colours and new ideas on pictures/positioning are welcome. I prefer a 'full width page' solution with centralised text elements but that's all up to you to suggest. Current site is a quickfix made by myself - now I'm moving it to a new platform so want to take the opportunity to make it
Nothing superspecial as it is a 2-man show; on the other hand I still want to have a modern & fresh reflection of my brand in digital environments. Help me out!
www.kelvora.se
Best
Lina Sjöbacka

```html
<!DOCTYPE html>
<html lang="en">
<head>
<meta charset="utf-8">
<title>Kelvora – Growth management consultancy</title>
<link href="https://fonts.googleapis.com/css2?family=Open+Sans:wght@400;600;700;800&display=swap" rel="stylesheet">
<style>
:root{
  --yellow:#fcd443;
  --ink:#151515;
  --text:#444;
  --muted:#9a9a9a;
  --page:#efefef;
  --white:#fff;
  --line:#d9d9d9;
  --teal:#6fc6c9;
  --green:#a9d89b;
}
*{box-sizing:border-box;margin:0;padding:0}
html,body{width:1200px;height:4328px;overflow:hidden}
body{background:var(--page);font-family:"Open Sans",Arial,sans-serif;color:var(--text);position:relative}
.abs{position:absolute}
a{color:inherit;text-decoration:none}

.mark{width:200px;height:200px;background:rgba(255,255,255,.55)}

/* header & hero */
.hero{left:0;top:0;width:1200px;height:572px;background:linear-gradient(180deg,#4d544d 0%,#6f7a70 45%,#5a6058 100%)}
.nav{left:160px;top:0;width:888px;height:80px;background:var(--ink);display:flex;align-items:center;justify-content:space-between;padding:0 24px}
.brand{font-weight:800;font-size:26px;color:var(--white);letter-spacing:-.5px}
.menu{display:flex;gap:22px;align-items:center;font-size:14px;font-weight:600;color:var(--white)}
.hero-title{left:0;top:232px;width:1200px;text-align:center;color:var(--white);font-weight:800;font-size:62px;letter-spacing:-1px}
.hero-sub{left:380px;top:320px;width:440px;text-align:center;color:#e8e8e8;font-size:19px;line-height:1.35}

/* yellow teaser band */
.band{left:0;top:572px;width:1200px;height:168px;background:var(--yellow)}
.teaser{top:600px;width:290px;height:112px;display:flex;gap:16px}
.teaser .thumb{width:100px;height:112px;background:linear-gradient(135deg,#5a5a5a,#2d2d2d);flex:none}
.teaser h3{font-size:16px;font-weight:800;color:var(--ink);line-height:1.2}
.teaser p{font-size:10px;color:#333;line-height:1.4;margin-top:6px}
.teaser .more{font-size:9px;font-weight:800;color:var(--ink);letter-spacing:.5px;margin-top:8px;display:block}

/* about */
.about-photo{left:160px;top:812px;width:540px;height:540px;background:linear-gradient(160deg,#d8d2c8,#a7a49c 55%,#7e7a73)}
.about-card{left:700px;top:900px;width:348px;height:432px;background:var(--white);padding:36px 30px}
.about-card h2{font-size:23px;font-weight:800;color:var(--ink);line-height:1.25}
.about-card p{font-size:12px;line-height:1.55;margin-top:18px}
.link-u{display:inline-block;margin-top:26px;font-size:11px;font-weight:800;color:var(--ink);letter-spacing:.8px;border-bottom:3px solid var(--yellow);padding-bottom:4px}

/* objective cards */
.frame{left:200px;top:1360px;width:760px;height:520px;border:8px solid var(--white)}
.obj{color:var(--white)}
.obj .ph{position:absolute;inset:0}
.obj h4{position:absolute;left:24px;font-size:18px;font-weight:800;line-height:1.25}
.btn-ghost{position:absolute;left:24px;border:2px solid var(--white);padding:6px 16px;font-size:13px;font-weight:600}
.explore{font-size:11px;font-weight:800;color:var(--ink);letter-spacing:.8px}

/* section headings */
.sec-title{left:0;width:1200px;text-align:center;font-size:24px;font-weight:700;letter-spacing:6px;color:#3a3a3a}

/* research */
.research{left:160px;top:2192px;width:888px;height:408px;background:var(--white)}
.research h3{position:absolute;left:48px;top:40px;font-size:28px;font-weight:700;color:var(--muted);line-height:1.2}
.research p{position:absolute;left:48px;top:128px;width:440px;font-size:13px;color:#b8b8b8;line-height:1.55}
.tl-label{top:2696px;width:110px;text-align:center;font-size:11px;color:#555;line-height:1.3}
.tl-label.on{font-weight:800;color:var(--ink)}

/* team */
.quote-box{left:160px;top:3080px;width:580px;height:480px;background:var(--yellow)}
.quote-box blockquote{position:absolute;left:40px;top:96px;width:296px;font-size:28px;font-weight:800;color:var(--ink);line-height:1.22}
.quote-box cite{position:absolute;left:40px;top:420px;font-style:normal;font-size:12px;color:#333}
.person{left:500px;top:3080px;width:240px;height:480px;background:linear-gradient(180deg,#cfcfcf,#6d6d6d)}
.testi{left:760px;top:3180px;width:288px;height:380px;background:var(--white);padding:28px 24px}
.testi .lbl{font-size:11px;font-weight:700;letter-spacing:3px;color:var(--muted)}
.testi q{display:block;margin-top:12px;font-size:17px;font-weight:800;color:var(--ink);line-height:1.3;quotes:"\201C" "\201D"}
.testi .who{position:absolute;left:24px;top:292px;display:flex;gap:12px;align-items:center}
.testi .avatar{width:60px;height:60px;background:linear-gradient(135deg,#bdbdbd,#777)}
.testi .who span{font-size:11px;line-height:1.4;color:#555}

/* contact */
.signup{left:320px;top:3920px;width:640px;height:72px;background:var(--white);border-radius:36px}
.signup .field{position:absolute;left:40px;top:25px;font-size:15px;color:#999}
.signup .go{position:absolute;right:8px;top:8px;width:180px;height:56px;border-radius:28px;background:var(--yellow);color:var(--ink);font-weight:800;font-size:16px;display:flex;align-items:center;justify-content:center}

footer{position:absolute;left:0;top:4100px;width:1200px;height:228px;background:var(--white)}
footer .brand{position:absolute;left:160px;top:100px;color:var(--ink);font-size:30px}
.fcol{position:absolute;top:84px;font-size:13px;line-height:1.55;color:#555}
.fcol h5{font-size:12px;font-weight:800;letter-spacing:3px;color:var(--ink);margin-bottom:6px}
</style>
</head>
<body>

<div class="abs mark" style="left:20px;top:1000px"></div>
<div class="abs mark" style="left:500px;top:1990px"></div>
<div class="abs mark" style="left:500px;top:2830px"></div>
<div class="abs mark" style="left:500px;top:3680px"></div>

<section class="abs hero" role="img" aria-label="Photo of a man working at a laptop in a bright office with plants"></section>
<nav class="abs nav">
  <span class="brand">Kelvora.</span>
  <div class="menu">
    <a>About</a><a>Solutions</a><a>Partners</a><a>News</a><a>Careers</a><a>Contact</a>
    <svg width="16" height="16" viewBox="0 0 16 16"><circle cx="6.5" cy="6.5" r="5" fill="none" stroke="#fff" stroke-width="2"/><line x1="10.5" y1="10.5" x2="15" y2="15" stroke="#fff" stroke-width="2"/></svg>
  </div>
</nav>
<h1 class="abs hero-title">Move forward.</h1>
<p class="abs hero-sub">Meet a team who embrace the best practices of strategy, consultancy, innovation and management to solve your toughest challenges.</p>

<div class="abs band"></div>
<article class="abs teaser" style="left:160px">
  <div class="thumb" role="img" aria-label="Photo of a manager at a desk"></div>
  <div><h3>Most common ways managers kill creativity.</h3><p>Small habits that quietly stop new ideas from growing.</p><a class="more">EXPLORE MORE</a></div>
</article>
<article class="abs teaser" style="left:460px">
  <div class="thumb" role="img" aria-label="Photo of a startup team meeting"></div>
  <div><h3>How to make your startup's workflow more effective.</h3><p>Simple steps to cut waste in daily work.</p><a class="more">EXPLORE MORE</a></div>
</article>
<article class="abs teaser" style="left:760px">
  <div class="thumb" role="img" aria-label="Photo of a workshop in progress"></div>
  <div><h3>Prioritize operational needs: Best practices.</h3><p>Focus your resources where growth really happens.</p><a class="more">EXPLORE MORE</a></div>
</article>

<div class="abs about-photo" role="img" aria-label="Photo of a seminar room with people seated, one leaning back with hands behind head"></div>
<section class="abs about-card">
  <h2>We are an independent consultancy firm in Stockholm specializing in growth management.</h2>
  <p>We are realizing your strategy into concrete actions and routines to help you "get ahead". We offer addressed consulting across several disciplines, supporting businesses influenced by a "fast forward" mindset.</p>
  <p style="margin-top:12px">Several managing roles in Global Operations and Business transformation have set us up with a broad range of competencies and a strong global profile.</p>
  <a class="link-u">KNOW MORE ABOUT US</a>
</section>

<div class="abs frame"></div>
<article class="abs obj" style="left:220px;top:1380px;width:340px;height:520px">
  <div class="ph" role="img" aria-label="Photo of a smiling man with glasses and arms crossed" style="background:linear-gradient(180deg,#d9d9d9,#7f8a95)"></div>
  <h4 style="top:396px">We all have objectives.<br>What are yours?</h4>
  <a class="btn-ghost" style="top:460px">Get started &nbsp;→</a>
</article>
<article class="abs obj" style="left:592px;top:1408px;width:348px;height:524px">
  <div class="ph" role="img" aria-label="Photo of a man and a woman standing in an office" style="background:linear-gradient(180deg,#b7b0a6,#5b5650)"></div>
  <h4 style="top:390px">Business is full of challenges.<br>What are yours?</h4>
  <a class="btn-ghost" style="top:452px">Get started &nbsp;→</a>
</article>
<a class="abs explore" style="left:460px;top:1892px">EXPLORE MORE</a>

<h2 class="abs sec-title" style="top:2064px">EXPERTISE &amp; PROCESS</h2>
<a class="abs" style="left:856px;top:2156px;font-size:13px;color:#333">⟶&nbsp; Project management</a>

<section class="abs research">
  <h3>Research<br>&amp; feasibility study</h3>
  <p>Lorem ipsum dolor sit amet, consectetur adipiscing elit, sed do eiusmod tempor incididunt ut labore et dolore magna aliqua. Ut enim ad minim veniam, quis nostrud exercitation ullamco laboris nisi ut aliquip ex ea commodo consequat. Duis aute irure dolor in reprehenderit in voluptate velit esse.</p>
  <svg class="abs" style="left:0;top:230px" width="888" height="178" viewBox="0 0 888 178">
    <path d="M0 178 C80 140 120 60 200 70 C280 80 300 150 380 150 C460 150 500 120 560 130 C640 145 700 160 888 170 L888 178Z" fill="var(--yellow)" opacity=".55"/>
    <path d="M0 178 C120 170 200 120 280 110 C360 100 400 60 460 50 C520 40 560 20 620 60 C680 100 740 150 888 160 L888 178Z" fill="var(--teal)" opacity=".45"/>
    <path d="M0 178 C100 160 160 140 240 130 C320 120 380 150 440 140 C520 125 600 110 660 130 C740 155 800 170 888 176 L888 178Z" fill="var(--green)" opacity=".5"/>
  </svg>
</section>

<svg class="abs" style="left:120px;top:2670px" width="960" height="20" viewBox="0 0 960 20">
  <line x1="20" y1="10" x2="940" y2="10" stroke="var(--line)" stroke-width="2"/>
  <line x1="20" y1="10" x2="400" y2="10" stroke="var(--yellow)" stroke-width="2"/>
  <g fill="#bbb"><circle cx="20" cy="10" r="5"/><circle cx="135" cy="10" r="5" fill="var(--yellow)"/><circle cx="250" cy="10" r="5" fill="var(--yellow)"/><circle cx="385" cy="10" r="5" fill="var(--teal)"/><circle cx="520" cy="10" r="5" fill="var(--teal)"/><circle cx="655" cy="10" r="5" fill="var(--green)"/><circle cx="790" cy="10" r="5"/><circle cx="925" cy="10" r="5"/></g>
</svg>
<span class="abs tl-label" style="left:85px">Say hello!</span>
<span class="abs tl-label on" style="left:200px">Research &amp; feasibility study</span>
<span class="abs tl-label" style="left:315px">Project management</span>
<span class="abs tl-label" style="left:450px">Analysis &amp; change</span>
<span class="abs tl-label" style="left:585px">Production process</span>
<span class="abs tl-label" style="left:720px">Concept development</span>
<span class="abs tl-label" style="left:855px">Pedagogical consulting</span>
<span class="abs tl-label" style="left:990px">Operational control</span>

<h2 class="abs sec-title" style="top:2896px">TEAM &amp; PEOPLE</h2>

<section class="abs quote-box">
  <blockquote>"I work for supporting businesses influenced by a 'fast forward' mindset and desire to optimize its operations."</blockquote>
  <cite>Lina Sjöbacka — Kelvora | Founder</cite>
</section>
<div class="abs person" role="img" aria-label="Cut-out photo of a smiling blonde woman in a dark blazer"></div>
<a class="abs explore" style="left:768px;top:3132px">EXPLORE MORE</a>
<section class="abs testi">
  <span class="lbl">TESTIMONIALS</span>
  <q>Jag uppskattar mycket att jobba med Kelvora &amp; Lina – hon kan verkligen konsten att konkretisera och få kommunikation att "lyfta."</q>
  <div class="who"><div class="avatar" role="img" aria-label="Portrait photo of a client"></div><span>Tobias Lindqvist — VD,<br>Informationschef Norrholm AB</span></div>
</section>

<h2 class="abs sec-title" style="top:3744px">GET IN TOUCH</h2>
<form class="abs signup"><span class="field">Please enter your E-mail</span><span class="go">Get started</span></form>

<footer>
  <span class="brand">Kelvora.</span>
  <div class="fcol" style="left:600px"><h5>CONTACT</h5>+46 (0) 701 23 45 67<br>info@kelvora.se</div>
  <div class="fcol" style="left:820px"><h5>SOCIAL</h5>Facenet<br>Linkwork</div>
  <svg class="abs" style="left:1024px;top:96px" width="16" height="24" viewBox="0 0 16 24"><path d="M8 22V3M2 9l6-6 6 6" fill="none" stroke="#333" stroke-width="2"/></svg>
</footer>

</body>
</html>
```